Single Page Timetracking Dashboard Desktop App UI Design (Figma Link required)

Main Idea: a SaaS tool where employees can add their time and project in a playful way. There is a infographics and a list with tasks as well.

Based on the attached concept.png the brief is following:

- check the attached rough scribble
- add own ideas or change things if they add value
- Style: colourful, nerdy, professional saas, modern, beautiful, white space
- Quality expectation: inspiration1+2.png
- I will need a Figma link
- desktop only
- make something fresh and unique

Process:
I need to include 2-3 feedback rounds that will span probably around 7 days

Target Market(s)

Internal Business Tool for a Software Development Company

Industry/Entity Type

IT

Other font styles liked:
• Could be monospace, not a must though

Requirements
Must have
• At least one page; Figma Link to the design;
Nice to have
• Microinterations like drop-down, hover/active colors; functionality specifications
Should not have
• Mobile view

```html
<!DOCTYPE html>
<html lang="en">
<head>
<meta charset="utf-8">
<title>Track Your Time</title>
<link href="https://fonts.googleapis.com/css2?family=Roboto+Mono:wght@400;500;700&family=Roboto:wght@400;500;700&display=swap" rel="stylesheet">
<style>
:root{
  --ink:#0e1020;
  --side:#0d0f1a;
  --bg:#f3f4f6;
  --white:#fff;
  --line:#e3e5ea;
  --muted:#9aa0ab;
  --text:#2c2f3a;
  --blue:#1d4ed8;
  --purple:#7c3aed;
  --purple-soft:#ede7fd;
  --yellow:#facc15;
  --magenta:#c026d3;
  --sky:#38bdf8;
  --pink:#ec4899;
  --teal:#2dd4bf;
  --chip:#f0f1f3;
}
*{box-sizing:border-box;margin:0;padding:0}
html,body{width:1149px;height:1200px;overflow:hidden;background:var(--side)}
.stage{position:absolute;left:0;top:0;width:1440px;height:1504px;transform:scale(.7979);transform-origin:0 0;font-family:"Roboto",sans-serif;color:var(--ink)}
.abs{position:absolute}
.mono{font-family:"Roboto Mono",monospace}
.sidebar{left:0;top:0;width:80px;height:1504px;background:var(--side)}
.nav-icon{left:26px;width:28px;height:28px}
.main{left:80px;top:8px;width:880px;height:1496px;background:var(--bg);border-radius:16px 0 0 0}
.aside{left:960px;top:8px;width:480px;height:1496px;background:var(--white)}
.h1{font-family:"Roboto Mono",monospace;font-weight:700;font-size:30px;letter-spacing:.5px}
.card{background:var(--white);border-radius:16px}
.c{transform:translate(-50%,-50%);text-align:center}
.cal-day{width:32px;height:32px;line-height:32px;font-size:13px;font-weight:500;text-align:center;border-radius:50%}
.cal-head{font-size:12px;font-weight:500;color:#555a66;width:40px;text-align:center}
.faded{color:#cfd2d8}
.field{border:1px solid var(--line);border-radius:6px;color:var(--muted);font-size:15px;padding:14px 19px}
.field svg{position:absolute;right:20px;top:17px}
.pill{width:64px;height:40px;border:1px solid var(--line);border-radius:6px;font-size:13px;display:flex;align-items:center;justify-content:center;background:#fff}
.pill.on{background:var(--purple-soft);border:2px solid var(--purple);color:var(--purple)}
.btn-grey{background:var(--chip);border-radius:6px;font-weight:700;display:flex;align-items:center;justify-content:center}
.btn-blue{background:var(--blue);color:#fff;border-radius:6px;font-weight:500;display:flex;align-items:center;justify-content:center;font-size:16px}
.legend-name{font-size:13px;color:#5b606b;display:flex;align-items:center;gap:8px}
.legend-name i{width:7px;height:7px;border-radius:50%}
.legend-val{font-family:"Roboto Mono",monospace;font-size:16px}
.view-more{color:var(--blue);font-weight:500;font-size:16px;display:flex;align-items:center;gap:10px}
.input{border:1px solid var(--line);border-radius:6px;height:40px;font-size:14px;color:var(--muted);display:flex;align-items:center;gap:10px;padding-left:14px}
.select{background:var(--chip);border-radius:6px;height:40px;font-size:14px;font-weight:500;display:flex;align-items:center;justify-content:space-between;padding:0 12px 0 20px}
.menu{background:#fff;border-radius:6px;box-shadow:0 4px 16px rgba(0,0,0,.08);padding:8px 0}
.menu div{height:40px;line-height:40px;padding-left:20px;font-size:14px}
.menu div.hl{background:#f6f6f8}
.day{font-family:"Roboto Mono",monospace;font-weight:700;color:var(--blue);letter-spacing:4px;font-size:15px}
.tag{height:26px;line-height:26px;padding:0 12px;border-radius:13px;font-size:14px;font-weight:500}
.tag.coding{background:#e0f2fe;color:#0ea5e9}
.tag.pm{background:#fae8ff;color:#c026d3}
.tag.meet{background:#ffedd5;color:#f97316}
.tag.design{background:#dcfce7;color:#16a34a}
.meta{right:32px;font-family:"Roboto Mono",monospace;font-size:14px;color:#6b7080}
.task-title{font-family:"Roboto Mono",monospace;font-weight:700;font-size:19px}
.task-desc{width:416px;font-size:16px;line-height:24px;color:var(--text)}
.mini{height:32px;background:var(--chip);border-radius:6px;font-size:12px;font-weight:700;display:flex;align-items:center;justify-content:center}
.divider{left:992px;width:416px;height:1px;background:var(--line)}
</style>
</head>
<body>
<div class="stage">

  <nav class="abs sidebar" aria-label="Main navigation">
    <svg class="abs nav-icon" style="top:98px" viewBox="0 0 28 28" fill="none" stroke="#fff" stroke-width="2.4"><circle cx="14" cy="14" r="10"/><path d="M14 8v6l4 3"/></svg>
    <svg class="abs nav-icon" style="top:170px" viewBox="0 0 28 28" fill="none" stroke="#fff" stroke-width="2.4"><path d="M4 24h20M6 24V14h5v10M11 24V6h6v18M17 24V12h5v12"/></svg>
    <svg class="abs nav-icon" style="top:242px" viewBox="0 0 28 28" fill="none" stroke="#fff" stroke-width="2.4"><path d="M3 8l3 3 5-5M3 19l3 3 5-5M14 9h11M14 20h11"/></svg>
    <svg class="abs nav-icon" style="top:314px" viewBox="0 0 28 28" fill="none" stroke="#fff" stroke-width="2.4"><circle cx="14" cy="14" r="11"/><circle cx="14" cy="11" r="4"/><path d="M7 22c2-4 12-4 14 0"/></svg>
    <svg class="abs nav-icon" style="top:1450px" viewBox="0 0 28 28" fill="none" stroke="#fff" stroke-width="2.4"><path d="M12 4H5v20h7M11 14h14M20 9l5 5-5 5"/></svg>
  </nav>

  <main class="abs main"></main>

  <h1 class="abs h1" style="left:112px;top:40px">Track Your Time</h1>
  <section class="abs card" style="left:112px;top:100px;width:816px;height:540px"></section>

  <div class="abs mono" style="left:144px;top:134px;font-size:20px;font-weight:500">October</div>
  <div class="abs btn-grey" style="left:352px;top:132px;width:28px;height:28px"><svg width="10" height="10" viewBox="0 0 10 10" fill="none" stroke="#000" stroke-width="2"><path d="M7 1L3 5l4 4"/></svg></div>
  <div class="abs btn-grey" style="left:388px;top:132px;width:28px;height:28px"><svg width="10" height="10" viewBox="0 0 10 10" fill="none" stroke="#000" stroke-width="2"><path d="M3 1l4 4-4 4"/></svg></div>

  <div class="abs cal-head c" style="left:160px;top:188px">MO</div>
  <div class="abs cal-head c" style="left:200px;top:188px">TU</div>
  <div class="abs cal-head c" style="left:240px;top:188px">WE</div>
  <div class="abs cal-head c" style="left:280px;top:188px">TH</div>
  <div class="abs cal-head c" style="left:320px;top:188px">FR</div>
  <div class="abs cal-head c" style="left:360px;top:188px">SA</div>
  <div class="abs cal-head c" style="left:400px;top:188px">SU</div>

  <div class="abs" style="left:144px;top:212px;width:280px;display:grid;grid-template-columns:repeat(7,40px);row-gap:8px;margin-left:-4px">
    <div class="cal-day">1</div><div class="cal-day">2</div><div class="cal-day">3</div><div class="cal-day">4</div><div class="cal-day">5</div><div class="cal-day">6</div><div class="cal-day">7</div>
    <div class="cal-day">8</div><div class="cal-day">9</div><div class="cal-day">10</div><div class="cal-day">11</div><div class="cal-day">12</div><div class="cal-day">13</div><div class="cal-day">14</div>
    <div class="cal-day">15</div><div class="cal-day">16</div><div class="cal-day">17</div><div class="cal-day">18</div><div class="cal-day">19</div><div class="cal-day">20</div><div class="cal-day">21</div>
    <div class="cal-day">22</div><div class="cal-day">23</div><div class="cal-day">24</div><div class="cal-day">25</div><div class="cal-day">26</div><div class="cal-day">27</div><div class="cal-day" style="background:var(--purple-soft);color:var(--purple)">28</div>
    <div class="cal-day" style="background:var(--blue);color:#fff">29</div><div class="cal-day">30</div><div class="cal-day">31</div><div class="cal-day faded">1</div><div class="cal-day faded">2</div><div class="cal-day faded">3</div><div class="cal-day faded">4</div>
  </div>

  <div class="abs field" style="left:448px;top:132px;width:448px;height:48px">Select project<svg width="14" height="14" viewBox="0 0 14 14" fill="none" stroke="#111" stroke-width="2"><path d="M2 5l5 5 5-5"/></svg></div>
  <div class="abs field" style="left:448px;top:196px;width:448px;height:48px">Select type<svg width="14" height="14" viewBox="0 0 14 14" fill="none" stroke="#111" stroke-width="2"><path d="M2 5l5 5 5-5"/></svg></div>
  <div class="abs field" style="left:448px;top:260px;width:448px;height:144px">What did you do?</div>

  <div class="abs pill on" style="left:144px;top:436px">1h</div>
  <div class="abs pill" style="left:220px;top:436px">2h</div>
  <div class="abs pill" style="left:296px;top:436px">3h</div>
  <div class="abs pill" style="left:372px;top:436px">4h</div>
  <div class="abs pill" style="left:144px;top:488px">5h</div>
  <div class="abs pill" style="left:220px;top:488px">6h</div>
  <div class="abs pill" style="left:296px;top:488px">7h</div>
  <div class="abs pill" style="left:372px;top:488px">8h</div>
  <div class="abs mono c" style="left:467px;top:482px;font-size:13px;font-weight:700;letter-spacing:1px">AND</div>
  <div class="abs pill" style="left:497px;top:436px">0m</div>
  <div class="abs pill" style="left:573px;top:436px">15m</div>
  <div class="abs pill on" style="left:497px;top:488px">30m</div>
  <div class="abs pill" style="left:573px;top:488px">45m</div>

  <div class="abs btn-grey" style="left:735px;top:436px;width:72px;height:40px;font-size:14px">– 5m</div>
  <div class="abs btn-grey" style="left:824px;top:436px;width:72px;height:40px;font-size:14px">+ 5m</div>
  <div class="abs mono" style="right:544px;top:484px;font-size:40px;font-weight:500;letter-spacing:1px">1h 30m</div>

  <div class="abs btn-grey" style="left:669px;top:560px;width:90px;height:48px;font-size:16px;font-weight:500">Reset</div>
  <div class="abs btn-blue" style="left:775px;top:560px;width:121px;height:48px">Save Task</div>

  <h2 class="abs h1" style="left:112px;top:708px">Statistics</h2>
  <div class="abs" style="left:822px;top:704px;width:106px;height:40px;background:#fff;border-radius:6px;font-size:14px;font-weight:500;display:flex;align-items:center;justify-content:center;gap:12px">Monate<svg width="10" height="10" viewBox="0 0 10 10" fill="none" stroke="#111" stroke-width="1.8"><path d="M1 3l4 4 4-4"/></svg></div>
  <section class="abs card" style="left:112px;top:768px;width:816px;height:704px"></section>

  <div class="abs mono" style="left:144px;top:802px;font-size:19px;font-weight:700">Current Month</div>
  <div class="abs mono" style="left:536px;top:802px;font-size:19px;font-weight:700">October</div>

  <svg class="abs" style="left:204px;top:852px" width="240" height="240" viewBox="0 0 240 240" role="img" aria-label="Current month hours per customer">
    <g transform="rotate(-90 120 120)" fill="none" stroke-width="36">
      <circle cx="120" cy="120" r="96" stroke="var(--purple)" stroke-dasharray="180.96 603.19" stroke-dashoffset="0"/>
      <circle cx="120" cy="120" r="96" stroke="var(--teal)" stroke-dasharray="60.32 603.19" stroke-dashoffset="-180.96"/>
      <circle cx="120" cy="120" r="96" stroke="var(--pink)" stroke-dasharray="120.64 603.19" stroke-dashoffset="-241.28"/>
      <circle cx="120" cy="120" r="96" stroke="var(--sky)" stroke-dasharray="60.32 603.19" stroke-dashoffset="-361.92"/>
      <circle cx="120" cy="120" r="96" stroke="var(--magenta)" stroke-dasharray="60.32 603.19" stroke-dashoffset="-422.24"/>
      <circle cx="120" cy="120" r="96" stroke="var(--yellow)" stroke-dasharray="120.64 603.19" stroke-dashoffset="-482.56"/>
    </g>
  </svg>

  <svg class="abs" style="left:596px;top:852px" width="240" height="240" viewBox="0 0 240 240" role="img" aria-label="October hours per customer, Customer B highlighted">
    <g transform="rotate(-90 120 120)" fill="none" stroke-width="36">
      <circle cx="120" cy="120" r="96" stroke="#ecfdfa" stroke-dasharray="60.32 603.19" stroke-dashoffset="-180.96"/>
      <circle cx="120" cy="120" r="96" stroke="#fce7f3" stroke-dasharray="120.64 603.19" stroke-dashoffset="-241.28"/>
      <circle cx="120" cy="120" r="96" stroke="#e0f2fe" stroke-dasharray="60.32 603.19" stroke-dashoffset="-361.92"/>
      <circle cx="120" cy="120" r="96" stroke="#fae8ff" stroke-dasharray="60.32 603.19" stroke-dashoffset="-422.24"/>
      <circle cx="120" cy="120" r="96" stroke="#fef9c3" stroke-dasharray="120.64 603.19" stroke-dashoffset="-482.56"/>
      <circle cx="120" cy="120" r="99" stroke="var(--purple)" stroke-width="42" stroke-dasharray="186.6 622.04"/>
    </g>
  </svg>
  <div class="abs" style="left:796px;top:898px;width:150px;height:50px;background:#fff;border-radius:6px;box-shadow:0 4px 14px rgba(0,0,0,.08);padding:8px 12px">
    <div class="legend-name" style="font-size:11px"><i style="background:var(--purple);width:6px;height:6px"></i>Customer B</div>
    <div class="mono" style="font-size:13px;margin-top:3px;padding-left:16px;margin-left:-4px">30h 45m (30%)</div>
  </div>

  <div class="abs mono" style="left:144px;top:1116px;font-size:16px;font-weight:700">Total: 111h 30m</div>
  <div class="abs mono" style="left:536px;top:1116px;font-size:16px;font-weight:700">Gesamt: 111h 30m</div>

  <div class="abs" style="left:144px;top:1162px;display:grid;grid-template-columns:188px 200px;row-gap:22px">
    <div><div class="legend-name"><i style="background:var(--yellow)"></i>Customer A</div><div class="legend-val" style="margin:8px 0 0 16px">20h 30m (20%)</div></div>
    <div><div class="legend-name"><i style="background:var(--purple)"></i>Customer B</div><div class="legend-val" style="margin:8px 0 0 16px">30h 45m (30%)</div></div>
    <div><div class="legend-name"><i style="background:var(--teal)"></i>Customer C</div><div class="legend-val" style="margin:8px 0 0 16px">10h 15m (10%)</div></div>
    <div><div class="legend-name"><i style="background:var(--pink)"></i>Customer D</div><div class="legend-val" style="margin:8px 0 0 16px">20h 30m (20%)</div></div>
    <div><div class="legend-name"><i style="background:var(--sky)"></i>Customer E</div><div class="legend-val" style="margin:8px 0 0 16px">10h 15m (10%)</div></div>
    <div><div class="legend-name"><i style="background:var(--magenta)"></i>Customer F</div><div class="legend-val" style="margin:8px 0 0 16px">10h 15m (10%)</div></div>
  </div>
  <div class="abs" style="left:536px;top:1162px;display:grid;grid-template-columns:188px 200px;row-gap:22px">
    <div><div class="legend-name"><i style="background:var(--yellow)"></i>Customer A</div><div class="legend-val" style="margin:8px 0 0 16px">20h 30m (20%)</div></div>
    <div><div class="legend-name"><i style="background:var(--purple)"></i>Customer B</div><div class="legend-val" style="margin:8px 0 0 16px">30h 45m (30%)</div></div>
    <div><div class="legend-name"><i style="background:var(--teal)"></i>Customer C</div><div class="legend-val" style="margin:8px 0 0 16px">10h 15m (10%)</div></div>
    <div><div class="legend-name"><i style="background:var(--pink)"></i>Customer D</div><div class="legend-val" style="margin:8px 0 0 16px">20h 30m (20%)</div></div>
    <div><div class="legend-name"><i style="background:var(--sky)"></i>Customer E</div><div class="legend-val" style="margin:8px 0 0 16px">10h 15m (10%)</div></div>
    <div><div class="legend-name"><i style="background:var(--magenta)"></i>Customer F</div><div class="legend-val" style="margin:8px 0 0 16px">10h 15m (10%)</div></div>
  </div>

  <div class="abs view-more" style="left:470px;top:1417px">View More<svg width="12" height="12" viewBox="0 0 12 12" fill="none" stroke="currentColor" stroke-width="2"><path d="M2 4l4 4 4-4"/></svg></div>

  <aside class="abs aside"></aside>
  <h2 class="abs h1" style="left:992px;top:40px">Your Tasks</h2>
  <div class="abs" style="left:1185px;top:44px;width:32px;height:32px;border-radius:50%;background:#fce7f3;color:var(--pink);font-size:15px;font-weight:500;display:flex;align-items:center;justify-content:center">5</div>

  <div class="abs input" style="left:992px;top:100px;width:200px"><svg width="18" height="18" viewBox="0 0 18 18" fill="none" stroke="#111" stroke-width="2"><circle cx="7.5" cy="7.5" r="5.5"/><path d="M12 12l4.5 4.5"/></svg>Search</div>
  <div class="abs input" style="left:1208px;top:100px;width:200px"><svg width="18" height="18" viewBox="0 0 18 18" fill="none" stroke="#111" stroke-width="1.8"><rect x="2" y="3" width="14" height="13" rx="2"/><path d="M2 7h14M6 1v4M12 1v4"/></svg>Select date range</div>

  <div class="abs select" style="left:992px;top:156px;width:128px">Sort by<svg width="12" height="12" viewBox="0 0 12 12" fill="none" stroke="#111" stroke-width="2"><path d="M2 4l4 4 4-4"/></svg></div>
  <div class="abs select" style="left:1136px;top:156px;width:128px">Project<svg width="12" height="12" viewBox="0 0 12 12" fill="none" stroke="#111" stroke-width="2"><path d="M2 4l4 4 4-4"/></svg></div>
  <div class="abs select" style="left:1280px;top:156px;width:128px">Type<svg width="12" height="12" viewBox="0 0 12 12" fill="none" stroke="#111" stroke-width="2"><path d="M2 4l4 4 4-4"/></svg></div>

  <div class="abs day" style="left:992px;top:231px">MONDAY</div>

  <div class="abs tag coding" style="left:992px;top:277px">Coding</div>
  <div class="abs task-title" style="left:992px;top:312px">Customer A - Project 1</div>
  <p class="abs task-desc" style="left:992px;top:347px">Lorem ipsum dolor sit amet consectetur. Interdum interdum gravida lorem bibendum congue lacus. Quis convallis sit cras faucibus lectus ipsum at.</p>
  <div class="abs mini" style="left:1276px;top:432px;width:53px">Edit</div>
  <div class="abs mini" style="left:1341px;top:432px;width:67px">Delete</div>
  <div class="abs divider" style="top:487px"></div>

  <div class="menu abs" style="left:1208px;top:204px;width:200px">
    <div class="hl">Coding</div><div>Project Management</div><div>Meeting</div>
  </div>

  <div class="abs tag pm" style="left:992px;top:513px">Project Management</div>
  <div class="abs meta" style="top:517px">2h 15m - October 29th</div>
  <div class="abs task-title" style="left:992px;top:548px">Customer A - Project 1</div>
  <p class="abs task-desc" style="left:992px;top:583px">Felis in ut elit morbi ornare pharetra. Morbi nec vitae sit posuere volutpat non lorem.</p>
  <div class="abs mini" style="left:1276px;top:644px;width:53px">Edit</div>
  <div class="abs mini" style="left:1341px;top:644px;width:67px">Delete</div>
  <div class="abs divider" style="top:699px"></div>

  <div class="abs tag meet" style="left:992px;top:725px">Meeting</div>
  <div class="abs meta" style="top:729px">1h - October 29th</div>
  <div class="abs task-title" style="left:992px;top:760px">Customer B - Project 1</div>
  <p class="abs task-desc" style="left:992px;top:795px">Mauris blandit dignissim non semper. Porttitor volutpat sit ultricies felis sit malesuada porttitor.</p>
  <div class="abs mini" style="left:1276px;top:856px;width:53px">Edit</div>
  <div class="abs mini" style="left:1341px;top:856px;width:67px">Delete</div>

  <div class="abs day" style="left:992px;top:947px">FRIDAY</div>

  <div class="abs tag design" style="left:992px;top:993px">Designing</div>
  <div class="abs meta" style="top:997px">5h - October 27th</div>
  <div class="abs task-title" style="left:992px;top:1028px">Customer A - Project 2</div>
  <p class="abs task-desc" style="left:992px;top:1063px">Arcu a vel orci quis magna lacinia lacus mollis. Aliquam vitae ut blandit viverra eget massa ac.</p>
  <div class="abs mini" style="left:1276px;top:1124px;width:53px">Edit</div>
  <div class="abs mini" style="left:1341px;top:1124px;width:67px">Delete</div>
  <div class="abs divider" style="top:1179px"></div>

  <div class="abs tag pm" style="left:992px;top:1205px">Project Management</div>
  <div class="abs meta" style="top:1209px">1h 30m - October 27th</div>
  <div class="abs task-title" style="left:992px;top:1240px">Customer B - Project 2</div>
  <p class="abs task-desc" style="left:992px;top:1275px">Mi condimentum erat eleifend aliquam tortor congue nisi quis sed. Lectus scelerisque bibendum egestas sociis auctor. Purus turpis diam ut ipsum.</p>
  <div class="abs mini" style="left:1276px;top:1360px;width:53px">Edit</div>
  <div class="abs mini" style="left:1341px;top:1360px;width:67px">Delete</div>

  <div class="abs view-more" style="left:1150px;top:1449px">View More<svg width="12" height="12" viewBox="0 0 12 12" fill="none" stroke="currentColor" stroke-width="2"><path d="M2 4l4 4 4-4"/></svg></div>

</div>
</body>
</html>
```